MMA fitness boot camp

We need a flyer that feels friendly and inviting to people who have never done fitness or training before. It also needs to look serious so it has the look of being a serious workout program.

We dont mind how it is set out as long as it conveys the message.

We do not want images of professional MMA fighters fighting. We like fitness training images that are relatable. eg- fit women punching or kicking a punching bag . If possible add men as well. We are aiming for men and women to do the boot camp.

The information for flyer is as below-

‘MMA Fitness Bootcamp’

Join us at Ironleaf Combat Studio for our new Mixed Martial Arts Bootcamp. You will train for 4 weeks with the same fitness methods a professional fighter would use before a fight! You will get an intense and challenging workout whilst having fun. This isn’t your common boot camp held at the local park, this is unique and enjoyable!

During this 4 week period, you will be training twice a week early mornings in our Training facility.

Enjoy training in a supportive environment with an MMA fighter and qualified Master trainer pushing you every session so that you get the best out of yourself.

For more information email us at marcus@ironleafcombatstudio.com.au or to book your spot with us.

or visit us at-
www.ironleafcombatstudio.com

ALL FITNESS LEVELS WELCOME!

Level 1, 274 Penrow Rd. Smithfield.'

```html
<!DOCTYPE html>
<html lang="en">
<head>
<meta charset="UTF-8">
<title>MMA Fitness Bootcamp – Ironleaf Combat Studio</title>
<link rel="stylesheet" href="https://fonts.googleapis.com/css2?family=Questrial&family=Didact+Gothic&display=swap">
<style>
  :root {
    --red: #d7202b;
    --orange: #f5911f;
    --ink: #3a3a3a;
    --white: #ffffff;
    --dark: #141414;
    --black: #111111;
  }
  * { margin: 0; padding: 0; box-sizing: border-box; }
  html, body { width: 1200px; height: 2609px; overflow: hidden; background: var(--white); }
  .flyer {
    position: relative;
    width: 1200px;
    height: 2609px;
    background: var(--white);
    font-family: "Questrial", "Didact Gothic", sans-serif;
    color: var(--ink);
    overflow: hidden;
  }
  .hero-photo {
    position: absolute;
    left: 0; top: 0;
    width: 1200px; height: 848px;
    background:
      radial-gradient(ellipse at 62% 40%, #5a4a44 0%, rgba(40,30,30,0) 45%),
      radial-gradient(ellipse at 30% 35%, #7a1c1e 0%, rgba(60,20,20,0) 40%),
      linear-gradient(100deg, #1a1a1a 0%, #2b2b2b 45%, #1c1c1c 100%);
  }
  .hero-rule {
    position: absolute;
    left: 0; top: 846px;
    width: 1200px; height: 9px;
    background: var(--red);
  }
  .url-band {
    position: absolute;
    left: 0; top: 22px;
    width: 1200px; height: 72px;
    background: var(--red);
    color: var(--white);
    font-size: 46px;
    letter-spacing: 1px;
    text-align: center;
    line-height: 72px;
    font-weight: 400;
  }
  .brand {
    position: absolute;
    left: 0; top: 905px;
    width: 1200px;
    display: flex;
    justify-content: center;
    align-items: center;
    gap: 22px;
    color: var(--orange);
    font-size: 64px;
    height: 180px;
  }
  .brand-mark {
    width: 44px; height: 44px;
    background: var(--orange);
  }
  .title {
    position: absolute;
    left: 0; top: 1118px;
    width: 1200px;
    text-align: center;
    color: var(--red);
    font-size: 86px;
    font-weight: 400;
    line-height: 1;
  }
  .welcome {
    position: absolute;
    left: 0; top: 1220px;
    width: 1200px;
    text-align: center;
    color: var(--orange);
    font-size: 45px;
    line-height: 1;
  }
  .body-copy {
    position: absolute;
    left: 70px; top: 1292px;
    width: 1060px;
    text-align: center;
    font-size: 40.5px;
    line-height: 59px;
    color: var(--ink);
  }
  .body-copy p + p { margin-top: 59px; }
  .journey {
    position: absolute;
    left: 0; top: 2203px;
    width: 1200px;
    text-align: center;
    color: var(--red);
    font-size: 52px;
    line-height: 1;
  }
  .more-info {
    position: absolute;
    left: 0; top: 2318px;
    width: 1200px;
    text-align: center;
    font-size: 31px;
    font-style: italic;
    letter-spacing: 1px;
    color: var(--black);
  }
  .footer {
    position: absolute;
    left: 0; top: 2440px;
    width: 1200px; height: 169px;
    background: var(--orange);
  }
  .book-button {
    position: absolute;
    left: 321px; top: 2388px;
    width: 561px; height: 104px;
    background: var(--white);
    border: 4px solid var(--black);
    border-radius: 6px;
    color: var(--red);
    font-size: 48px;
    text-align: center;
    line-height: 96px;
  }
  .contact {
    position: absolute;
    left: 0; top: 2510px;
    width: 1200px;
    text-align: center;
    color: var(--white);
    font-size: 36px;
    line-height: 52px;
  }
</style>
</head>
<body>
  <main class="flyer">
    <div class="hero-photo" role="img" aria-label="Woman in boxing gloves punching a heavy bag against a dark gym backdrop"></div>
    <div class="hero-rule"></div>
    <div class="url-band">WWW.IRONLEAFCOMBATSTUDIO.COM</div>

    <div class="brand">
      <span class="brand-mark"></span>
      <span class="brand-name">Ironleaf Combat Studio</span>
    </div>

    <h1 class="title">MMA Fitness Bootcam</h1>
    <div class="welcome">- ALL FITNESS LEVELS WELCOME! -</div>

    <div class="body-copy">
      <p>Join us at Ironleaf Combat Studio for our new Mixed Martial Arts Bootcamp. You will train for 4 weeks with the same fitness methods a professional fighter would use before a fight! You will get an intense and challenging workout whilst having fun. This isn’t your common boot camp held at the local park, this is unique and enjoyable!</p>
      <p>During this 4 week period, you will be training twice a week early mornings in our Training facility.</p>
      <p>Enjoy training in a supportive environment with an MMA fighter and qualified Master trainer pushing you every session so that you get the best out of yourself.</p>
    </div>

    <div class="journey">Let us being a part of your training journey!</div>
    <div class="more-info">FOR MORE INFORMATION EMAIL US OR VISIT OUR SITE</div>

    <div class="footer"></div>
    <div class="book-button">BOOK YOUR SPOT!</div>
    <div class="contact">
      e-mail: marcus@ironleafcombatstudio.com.au<br>
      address: Level 1, 274 Penrow Rd. Smithfield
    </div>
  </main>
</body>
</html>
```